Test and Tag business card design

We are an appliance test and tag company in Brisbane Australia requiring a business card design.
I don't have a logo.
Card front: Matte black background with white font.
Card back: White background with black font colour
Examples are attached
Minimalist design
Reason: Looking for more designs with an extreme minimal feel
Industry/Entity Type
Appliance
Contact Information for Business Card
Business name: Harbor Check and Label
Description: Onsite Electrical Testing and Tagging
Licence No. 41853
Name: Greg Pellow
Mobile: 0418 526 937
Email: greg@harborcheckandlabel.com.au
Web: harborcheckandlabel.com.au
Logo Text
Harbor Check and Label
Look and feel

```html
<!DOCTYPE html>
<html lang="en">
<head>
<meta charset="utf-8">
<title>Harbor Check and Label — Business Card</title>
<link rel="stylesheet" href="https://fonts.googleapis.com/css2?family=Orbitron:wght@500;600;700&display=swap">
<style>
  :root {
    --paper: #ffffff;
    --card: #000000;
    --ink: #ffffff;
  }
  html, body {
    margin: 0;
    padding: 0;
    width: 1200px;
    height: 693px;
    overflow: hidden;
    background: var(--paper);
  }
  .business-card {
    display: block;
    width: 1200px;
    height: 693px;
  }
  .card-face { fill: var(--card); }
  .divider { fill: var(--ink); }
  .card-text {
    fill: var(--ink);
    font-family: "Orbitron", sans-serif;
    text-anchor: middle;
  }
  .company-name { font-size: 54px; font-weight: 700; }
  .tagline { font-size: 27px; font-weight: 600; }
  .person-name { font-size: 46px; font-weight: 700; }
  .contact-line { font-size: 27px; font-weight: 600; }
  .licence { font-size: 38px; font-weight: 700; }
</style>
</head>
<body>
<svg class="business-card" viewBox="0 0 1200 693" xmlns="http://www.w3.org/2000/svg">
  <rect class="card-face" x="20" y="20" width="1160" height="653"/>

  <text class="card-text company-name" x="600" y="148" textLength="970" lengthAdjust="spacingAndGlyphs">HARBOR CHECK AND LABEL</text>
  <text class="card-text tagline" x="600" y="195" textLength="976" lengthAdjust="spacingAndGlyphs">ONSITE ELECTRICAL TESTING AND TAGGING</text>

  <rect class="divider" x="413" y="200" width="4" height="458"/>

  <text class="card-text person-name" x="220" y="384">GREG</text>
  <text class="card-text person-name" x="220" y="466">PELLOW</text>

  <text class="card-text contact-line" x="792" y="364">MOBILE: 0418 526 937</text>
  <text class="card-text contact-line" x="792" y="420" textLength="640" lengthAdjust="spacingAndGlyphs">EMAIL: GREG@HARBORCHECKANDLABEL.COM.AU</text>
  <text class="card-text contact-line" x="792" y="475" textLength="560" lengthAdjust="spacingAndGlyphs">WEB: HARBORCHECKANDLABEL.COM.AU</text>

  <text class="card-text licence" x="792" y="589" textLength="505" lengthAdjust="spacingAndGlyphs">LICENCE NO. 41853</text>
</svg>
</body>
</html>
```